Conservative, Modern and Sharp Builder Business card

Hi there,
We would like to update our existing business card.
I have attached photos of existing business card, logo and van sign.

I would like the business card to also list what we do :
Renovation • New Build • Alteration
Extension • Bathroom • Maintenance.(Seperated by dots)

Contact number : 021 0483 0752
(With that exact spacing)

Ideally when people looking from about 2-3 metres, they know that it is a builder’s business card

Open to suggestions on fonts, layout, style of business card

PLEASE ONLY SUBMIT YOUR BEST OR MAX 3 DESIGNS FOR EACH DESIGNER

Thanks

Industry/Entity Type

Construction. Renovation

Contact Information for Business Card

Details should be the same as the existing card. And addition of what we do.

Requirements
Should not have
• The new business card must not have the same layout as our existing one. Thanks

```html
<!DOCTYPE html>
<html lang="en">
<head>
<meta charset="utf-8">
<title>KeelCraft Business Card</title>
<link href="https://fonts.googleapis.com/css2?family=Montserrat:wght@300;400;600;700;800&display=swap" rel="stylesheet">
<style>
  :root {
    --backdrop: #e9e6e1;
    --card: #ffffff;
    --ink: #1c1c1c;
    --ink-soft: #3a3a3a;
    --rule: #8a8a8a;
  }
  * { box-sizing: border-box; margin: 0; padding: 0; }
  html, body { width: 1200px; height: 900px; overflow: hidden; }
  body {
    background: var(--backdrop);
    font-family: "Montserrat", Arial, sans-serif;
    color: var(--ink);
    position: relative;
  }
  .card {
    position: absolute;
    left: 290px;
    width: 620px;
    height: 354px;
    background: var(--card);
    box-shadow: 0 6px 18px rgba(0,0,0,0.18);
    overflow: hidden;
  }
  .card--back { top: 70px; }
  .card--front { top: 476px; }

  .wordmark {
    position: absolute;
    display: flex;
    align-items: center;
    gap: 10px;
    font-weight: 800;
    font-size: 40px;
    letter-spacing: -0.5px;
    color: var(--ink);
  }
  .wordmark__square {
    width: 26px; height: 26px;
    background: var(--ink);
  }
  .card--back .wordmark { right: 40px; bottom: 48px; }
  .card--front .wordmark { right: 36px; top: 40px; }

  .web-spaced {
    position: absolute;
    left: 36px; top: 30px;
    font-size: 13px;
    letter-spacing: 4px;
    color: var(--ink-soft);
  }

  .person {
    position: absolute;
    left: 36px; top: 168px;
  }
  .person__name { font-weight: 700; font-size: 19px; letter-spacing: 1px; }
  .person__role { font-weight: 400; font-size: 15px; color: var(--ink-soft); margin-top: 4px; letter-spacing: 0.5px; }

  .contact {
    position: absolute;
    left: 36px; top: 238px;
  }
  .contact__row { display: flex; align-items: center; gap: 8px; }
  .contact__phone { font-weight: 600; font-size: 21px; letter-spacing: 0.5px; }
  .contact__mail { font-size: 15px; color: var(--ink-soft); margin-top: 6px; }
  .contact svg { flex: none; }

  .online {
    position: absolute;
    left: 360px; top: 196px;
    padding-left: 14px;
    border-left: 1.5px solid var(--ink-soft);
    font-size: 15px;
    color: var(--ink-soft);
    line-height: 1.6;
  }
  .online__row { display: flex; align-items: center; gap: 8px; }
  .online__dot {
    width: 13px; height: 13px; border-radius: 50%;
    border: 1.5px solid var(--ink-soft);
  }
  .online-rule {
    position: absolute; left: 360px; right: 28px; top: 182px;
    border-top: 1px solid var(--rule);
  }

  .services-rule {
    position: absolute; left: 0; right: 0; bottom: 46px;
    border-top: 1px solid var(--rule);
  }
  .services {
    position: absolute; left: 36px; right: 36px; bottom: 16px;
    display: flex;
    justify-content: space-between;
    font-size: 14px;
    color: var(--ink-soft);
    white-space: nowrap;
  }
  .services__dot { color: var(--ink); }
</style>
</head>
<body>

  <section class="card card--back">
    <div class="web-spaced">www.KeelCraft.nz</div>
    <div class="wordmark"><span class="wordmark__square"></span>KeelCraft</div>
  </section>

  <section class="card card--front">
    <div class="wordmark"><span class="wordmark__square"></span>KeelCraft</div>

    <div class="person">
      <div class="person__name">DARIN HOLLOWAY</div>
      <div class="person__role">Residential Builder</div>
    </div>

    <div class="contact">
      <div class="contact__row contact__phone">
        <svg width="16" height="16" viewBox="0 0 24 24" aria-hidden="true"><path fill="#1c1c1c" d="M6.6 10.8a15.1 15.1 0 0 0 6.6 6.6l2.2-2.2c.3-.3.7-.4 1-.2 1.1.4 2.3.6 3.6.6.6 0 1 .4 1 1V20c0 .6-.4 1-1 1A17 17 0 0 1 3 4c0-.6.4-1 1-1h3.5c.6 0 1 .4 1 1 0 1.3.2 2.5.6 3.6.1.3 0 .7-.2 1z"/></svg>
        021 0483 0752
      </div>
      <div class="contact__row contact__mail">
        <svg width="16" height="14" viewBox="0 0 24 20" aria-hidden="true"><rect x="1" y="2" width="22" height="16" rx="2" fill="#1c1c1c"/><path d="M2 4l10 7 10-7" stroke="#fff" stroke-width="2" fill="none"/></svg>
        KeelCraft@mailbox.nz
      </div>
    </div>

    <div class="online-rule"></div>
    <div class="online">
      <div class="online__row"><span class="online__dot"></span>KeelCraft.nz</div>
      <div class="online__row"><span class="online__dot"></span>www.KeelCraft.nz</div>
    </div>

    <div class="services-rule"></div>
    <div class="services">
      <span>Renovation</span><span class="services__dot">•</span>
      <span>New Build</span><span class="services__dot">•</span>
      <span>Alteration</span><span class="services__dot">•</span>
      <span>Extension</span><span class="services__dot">•</span>
      <span>Bathroom</span><span class="services__dot">•</span>
      <span>Maintenance</span>
    </div>
  </section>

</body>
</html>
```